Flyer / marketing email used to solicate work for specialized tree removal equipment.

I'm looking for a flyer for door to door and direct mail distributon. Please utilize as much of the following verbiage as possible...

Breaking news!¿the only 170' grapple crane in use in North American is coming to your neighborhood This revolutionary technology will be in your area for a limited time. Our equipment allows to us accomplish the most challenging tree scenarios with no climber, limited personnel, and amazing efficiency.

This innovation has completely changed the cost of hazardous removals. Call now to get the most competitive estimate yet.

This technology is so limited and in high demand that it can only be in your area for a short time before it has to move on. Get on the list today, it may be months before it makes another round to your neighborhood. ¿

Target Market(s)

Flyers will be delivered in a high end residential neighborhood. Distribution will be on heavy stock and via email.

Colors

Designer to choose colors to be used in the design.

Requirements
Must have
• My logo. Pictures of the crane equipment. Pictures of other tree equipment.
• I'd like a two sided 4" x 5.5" mailer.
• I have permissions to utilize content from the sample one fold flyers I have uploaded.
• I'd like a majority of the content of the Vortalix (aka. Plover limb sample). The light background of the 842 Boughs sample.
• A "BLACK FRIDAY SALE" theme would be awesome.
Nice to have
• Old time breaking news headline married with a high tech innovative feel
• OR
• BLACK FRIDAY SALE theme.

```html
<!DOCTYPE html>
<html lang="en">
<head>
<meta charset="utf-8">
<title>Thornwick Tree Care – Grapple Crane Flyer</title>
<link href="https://fonts.googleapis.com/css2?family=Bebas+Neue&family=Fira+Sans+Condensed:wght@400&family=Roboto+Condensed:wght@400;500&display=swap" rel="stylesheet">
<style>
  :root {
    --page-bg: #e6e8ec;
    --paper: #f1f2f5;
    --brand-blue: #3d64a6;
    --lime: #a9c83a;
    --ink: #1d1d1f;
    --forest: #2f4a1f;
    --white: #ffffff;
  }
  * { margin: 0; padding: 0; box-sizing: border-box; }
  html, body { width: 1200px; height: 1200px; overflow: hidden; background: var(--page-bg); }
  .flyer {
    position: absolute; left: 176px; top: 0; width: 848px; height: 1200px;
    background: var(--paper); overflow: hidden;
  }
  .hero {
    position: absolute; left: 0; top: 0; width: 848px; height: 265px;
    background: linear-gradient(160deg, #5d7fa6 0%, #3f6a80 40%, #2f5a4a 75%, #4d6c8a 100%);
  }
  .hero-title {
    position: absolute; left: 0; width: 848px; top: 84px; text-align: center;
    font-family: "Bebas Neue", sans-serif; font-size: 50px; line-height: 1;
    color: var(--white); white-space: nowrap; padding-right: 140px;
  }
  .hero-title .accent { color: var(--lime); }
  .hero-sub {
    position: absolute; left: 0; width: 848px; top: 138px; text-align: center; padding-right: 140px;
    font-family: "Bebas Neue", sans-serif; font-size: 26px; line-height: 1; color: var(--white); white-space: nowrap;
  }
  .hero-copy {
    position: absolute; left: 0; width: 848px; top: 172px; text-align: center; padding-right: 140px;
    font-family: "Fira Sans Condensed", sans-serif; font-size: 18px; line-height: 22.5px; color: var(--white);
    letter-spacing: 0.3px; white-space: nowrap;
  }
  .gallery { position: absolute; left: 0; top: 265px; }
  .brand {
    position: absolute; left: 420px; width: 380px; top: 405px; text-align: center;
    font-family: "Roboto Condensed", sans-serif; color: var(--forest);
  }
  .brand-name { font-size: 34px; font-weight: 500; line-height: 1; }
  .brand-place { font-size: 15px; font-weight: 500; margin-top: 8px; letter-spacing: 1px; }
  .copy {
    position: absolute; left: 0; top: 0;
    font-family: "Roboto Condensed", sans-serif; font-size: 21px; color: var(--ink);
    text-transform: uppercase; white-space: nowrap;
  }
  .copy span { position: absolute; line-height: 1; }
  .cta-heading {
    position: absolute; left: 352px; top: 902px;
    font-family: "Roboto Condensed", sans-serif; font-size: 46px; color: var(--brand-blue);
    white-space: nowrap; letter-spacing: 1px;
  }
  .phone-pill {
    position: absolute; left: 385px; top: 978px; width: 373px; height: 59px; border-radius: 30px;
    background: var(--brand-blue); color: var(--white);
    display: flex; align-items: center; padding-left: 16px; gap: 14px;
    font-family: "Roboto Condensed", sans-serif; font-size: 38px; letter-spacing: 1px;
  }
  .footer {
    position: absolute; left: 0; top: 1121px; width: 848px; height: 79px; background: var(--brand-blue);
    color: var(--white); font-family: "Roboto Condensed", sans-serif; font-size: 32px;
  }
  .footer-pin { position: absolute; left: 26px; top: 12px; }
  .footer-address { position: absolute; left: 79px; top: 10px; line-height: 29px; white-space: nowrap; letter-spacing: 1px; }
  .footer-web { position: absolute; left: 456px; top: 24px; white-space: nowrap; letter-spacing: 1px; }
</style>
</head>
<body>
<main class="flyer">
  <header class="hero" role="img" aria-label="Photo of a long grapple crane boom arching over a residential street">
    <h1 class="hero-title">The only <span class="accent">170' grapple crane</span></h1>
    <p class="hero-sub">In North American is coming to your neighborhood</p>
    <p class="hero-copy">This revolutionary technology will be in your area for a limited time.<br>Our equipment allows to us accomplish the most challenging tree<br>scenarios with no climber, limited personnel, and amazing efficiency.</p>
  </header>

  <svg class="gallery" width="848" height="856" viewBox="0 0 848 856" aria-hidden="false">
    <defs>
      <clipPath id="photo-edge">
        <path d="M0 0 H343 C385 60 400 140 396 207 C392 330 340 440 315 507 C300 560 292 610 296 667 C300 740 312 800 315 856 H0 Z"/>
      </clipPath>
      <linearGradient id="sky" x1="0" y1="0" x2="0" y2="1">
        <stop offset="0" stop-color="#5b8fd6"/><stop offset="0.7" stop-color="#8fb5e8"/><stop offset="1" stop-color="#3d5a3a"/>
      </linearGradient>
      <linearGradient id="street" x1="0" y1="0" x2="1" y2="1">
        <stop offset="0" stop-color="#3f5a44"/><stop offset="1" stop-color="#7c8f98"/>
      </linearGradient>
      <linearGradient id="yard" x1="0" y1="0" x2="0" y2="1">
        <stop offset="0" stop-color="#8a8672"/><stop offset="1" stop-color="#4b4d3c"/>
      </linearGradient>
    </defs>
    <g clip-path="url(#photo-edge)">
      <rect x="0" y="0" width="400" height="507" fill="url(#sky)" role="img" aria-label="Photo of a blue grapple crane gripping the top of a tall pine tree"/>
      <rect x="0" y="507" width="400" height="132" fill="url(#street)" role="img" aria-label="Photo of the crane boom extended above rooftops"/>
      <rect x="0" y="639" width="400" height="217" fill="url(#yard)" role="img" aria-label="Photo of the crane boom beside a bucket truck at a house"/>
      <line x1="0" y1="507" x2="400" y2="507" stroke="#ffffff" stroke-width="1.5"/>
      <line x1="0" y1="639" x2="400" y2="639" stroke="#ffffff" stroke-width="1.5"/>
    </g>
  </svg>

  <div class="brand">
    <div class="brand-name">Thornwick Tree Care</div>
    <div class="brand-place">-- CEDAR BEND, MI --</div>
  </div>

  <div class="copy">
    <span style="left:411px;top:502px">This revolutionary technology will be</span>
    <span style="left:411px;top:526px">in your area for a limited time.</span>
    <span style="left:411px;top:549px">Our equipment allows to us accomplish</span>
    <span style="left:405px;top:573px">the most challenging tree scenarios</span>
    <span style="left:399px;top:597px">with no climber, limited personnel,</span>
    <span style="left:393px;top:620px">and amazing efficiency.</span>
    <span style="left:387px;top:643px">This innovation has completely changed the</span>
    <span style="left:382px;top:665px">cost of hazardous removals. Call now to get</span>
    <span style="left:376px;top:688px">the most competitive estimate yet.</span>
    <span style="left:330px;top:771px">This technology is so limited and in high&nbsp; demand</span>
    <span style="left:324px;top:796px">that it can only be in your area for a short time</span>
    <span style="left:319px;top:820px">before it has to move on.</span>
  </div>

  <h2 class="cta-heading">GET ON THE LIST TODAY,</h2>
  <div class="phone-pill">
    <svg width="46" height="46" viewBox="0 0 24 24" fill="none" stroke="#ffffff" stroke-width="1.4" stroke-linejoin="round">
      <path d="M5 3h4l2 5-2.5 1.5a11 11 0 0 0 6 6L16 13l5 2v4a2 2 0 0 1-2 2A17 17 0 0 1 3 5a2 2 0 0 1 2-2z"/>
    </svg>
    <span>(000)12345678</span>
  </div>

  <footer class="footer">
    <svg class="footer-pin" width="34" height="50" viewBox="0 0 34 50">
      <path d="M17 0C7.6 0 0 7.4 0 16.6 0 29 17 50 17 50s17-21 17-33.4C34 7.4 26.4 0 17 0z" fill="#ffffff"/>
      <circle cx="17" cy="16" r="7" fill="#3d64a6"/>
    </svg>
    <div class="footer-address">215&nbsp; MAPLE ROW<br>FERNBROOK</div>
    <div class="footer-web">WWW.COMPANYNAME.COM</div>
  </footer>
</main>
</body>
</html>
```